MRHT Needs Fundraiser Dinner Invite!!

The Marisol Hendrick Trust, a 501 3(c) non for profit has a yearly fundraiser, with varying themes. Last year it was "cowboys" and "cowgirls"
This year, it is Club Orchid, or 70's disco music. I have uploaded last years invite for reference, some stock photography for inspiration. You are not limited to using the stock photos.

Annual MRHT Fundraiser Dinner
October 13th, 2022
Starts: 6:30pm
RSVP By: September 20th
Place: The Bramwell
Price: $135 per ticket

Target Market(s)

Donors, Business People, Every person

Industry/Entity Type

Non for Profit

Font styles to use
Sans Serif

Colors
0054AA
0677BA
7BADD7
CADEEF
E8F1F8
E54698
E96AAD
F1A4CE
F9D9EA
FCEFF6
6B429C
8869AF
B7A5CE
E3DAEB
F3F0F8

Requirements
Must have
• The invite should be 5x7, be sophisticated as the clientele are mainly business people that come to support the cause. It should be fun and inviting at the same time.

```html
<!DOCTYPE html>
<html lang="en">
<head>
<meta charset="utf-8">
<title>Annual MRHT Fundraiser Dinner</title>
<link rel="stylesheet" href="https://fonts.googleapis.com/css2?family=Anton&family=Passion+One:wght@700&display=swap">
<style>
  :root {
    --ink: #1e0b6a;
    --white: #ffffff;
    --pink-hot: #e5358f;
    --pink-soft: #f1a4ce;
    --blush: #f9d9ea;
    --aqua: #8ee6ee;
    --steel: #4a86b3;
    --denim: #33508e;
    --navy: #1f1a4d;
    --night: #0c0a1e;
    --glow: rgba(255, 255, 255, 0.55);
  }
  * { margin: 0; padding: 0; box-sizing: border-box; }
  html, body { width: 857px; height: 1200px; overflow: hidden; background: var(--night); }
  .invite {
    position: relative;
    width: 857px;
    height: 1200px;
    overflow: hidden;
    font-family: "Anton", "Arial Narrow", sans-serif;
    color: var(--ink);
  }
  .invite p, .invite span, .invite h1 { white-space: nowrap; }
  .backdrop-photo {
    position: absolute;
    inset: 0;
    background:
      linear-gradient(180deg, rgba(0,0,0,0) 0%, rgba(0,0,0,0) 52%, rgba(20,14,50,0.65) 66%, var(--night) 80%, var(--navy) 100%),
      linear-gradient(90deg, var(--pink-soft) 0%, var(--blush) 12%, var(--pink-soft) 20%, var(--aqua) 26%, var(--blush) 34%, var(--pink-soft) 45%, var(--blush) 60%, var(--steel) 75%, var(--denim) 88%, var(--navy) 100%);
  }
  .backdrop-record {
    position: absolute;
    left: 0; top: 630px;
    width: 857px; height: 300px;
    background: linear-gradient(180deg, var(--pink-hot) 0%, #c21f70 55%, rgba(12,10,30,0) 100%);
    opacity: 0.85;
  }
  .backdrop-reflection {
    position: absolute;
    left: 0; top: 1030px;
    width: 420px; height: 70px;
    background: linear-gradient(90deg, var(--pink-hot) 0%, #b03ab0 45%, #4d7fd0 70%, rgba(31,26,77,0) 100%);
    filter: blur(10px);
    opacity: 0.9;
  }
  .headline, .details { position: absolute; inset: 0; text-transform: uppercase; line-height: 1; }
  .shadowed { text-shadow: 1px 2px 3px var(--glow); }
  .kicker { position: absolute; left: 49px; top: 30px; font-size: 39px; font-family: "Passion One", sans-serif; }
  .title {
    position: absolute; left: 40px; top: 56px;
    font-family: "Passion One", sans-serif;
    font-size: 250px; letter-spacing: -4px; line-height: 1; font-weight: 700;
  }
  .event { position: absolute; left: 45px; top: 282px; font-size: 54px; letter-spacing: 0.5px; }
  .place { position: absolute; left: 45px; top: 350px; font-size: 42px; letter-spacing: 0.5px; }
  .date { position: absolute; left: 43px; top: 484px; font-size: 53px; letter-spacing: 0.5px; }
  .time { position: absolute; left: 43px; top: 540px; font-size: 50px; letter-spacing: 0.5px; }
  .price-badge {
    position: absolute; left: 580px; top: 383px;
    width: 245px; height: 231px; border-radius: 50%;
    background: var(--white);
    display: flex; flex-direction: column; align-items: center; justify-content: center;
    text-transform: uppercase; line-height: 1.05; text-align: center;
    padding-bottom: 24px;
  }
  .price-label { font-size: 32px; }
  .price-amount { font-size: 32px; }
  .rsvp { position: absolute; right: 26px; top: 1086px; text-align: right; color: var(--white); text-transform: uppercase; line-height: 1; }
  .rsvp-title { font-size: 44px; }
  .rsvp-date { font-size: 45px; margin-top: 6px; }
  .site { position: absolute; left: 44px; top: 1116px; display: flex; align-items: center; gap: 14px; color: var(--white); text-transform: uppercase; line-height: 1; }
  .site-mark { width: 56px; height: 56px; border-radius: 50%; background: var(--white); opacity: 0.9; }
  .site-name { font-size: 34px; letter-spacing: 0.5px; }
</style>
</head>
<body>
<main class="invite">
  <div class="backdrop-photo" role="img" aria-label="Disco-lit photograph of a turntable playing a vinyl record under pink, aqua and blue stage lights"></div>
  <div class="backdrop-record" aria-hidden="true"></div>
  <div class="backdrop-reflection" aria-hidden="true"></div>

  <header class="headline">
    <p class="kicker shadowed">Annual</p>
    <h1 class="title shadowed">MRHT</h1>
  </header>

  <section class="details">
    <p class="event shadowed">Fundraiser Dinner</p>
    <p class="place shadowed">Place: The Bramwell</p>
    <p class="date shadowed">October 13th, 2022</p>
    <p class="time shadowed">Starts: 6:30 PM</p>
  </section>

  <aside class="price-badge">
    <span class="price-label shadowed">Price</span>
    <span class="price-amount shadowed">$135 per ticket</span>
  </aside>

  <footer>
    <div class="site">
      <span class="site-mark" aria-hidden="true"></span>
      <span class="site-name">MRHT.ORG</span>
    </div>
    <div class="rsvp">
      <p class="rsvp-title">RSVP</p>
      <p class="rsvp-date">By September 20th</p>
    </div>
  </footer>
</main>
</body>
</html>
```